Stationery Design Project - New innovative law firm

I need a simple design, yet the tone of the stationery set need to express modern, professionalism, smart and forward-thinking. I don’t need a business card, but require the stationery set to have:
• Design letterhead
• Design facsimile
• Design memo
The triangular logo with Corvane Associates words etc, need to be present in the stationery. The red triangular logo should not be re-designed, but feel free to play around with the placement and colours of the Corvane Associates words etc....?

Target Market(s)

Business clients

Industry/Entity Type

Business

Requirements
Must have
• The triangular logo with Corvane Associates words etc...for branding.

```html
<!DOCTYPE html>
<html lang="en">
<head>
<meta charset="utf-8">
<title>Corvane Associates – Letterhead</title>
<link rel="stylesheet" href="https://fonts.googleapis.com/css2?family=Open+Sans:wght@400;700&family=Arimo:wght@400;700&display=swap">
<style>
  :root {
    --brand-red: #d8261e;
    --ink-black: #0e0e10;
    --ink-grey: #6a6a6a;
    --paper: #ffffff;
    --footer-text: #ffffff;
  }
  * { margin: 0; padding: 0; box-sizing: border-box; }
  html, body { width: 917px; height: 1200px; overflow: hidden; background: var(--paper); }
  .letterhead {
    position: relative;
    width: 917px;
    height: 1200px;
    background: var(--paper);
    overflow: hidden;
  }
  .brand {
    position: absolute;
    left: 80px;
    top: 36px;
    display: flex;
    align-items: center;
    gap: 18px;
  }
  .brand-mark {
    width: 58px;
    height: 58px;
    background: var(--brand-red);
  }
  .brand-text { display: flex; flex-direction: column; }
  .brand-name {
    font-family: "Open Sans", sans-serif;
    font-weight: 700;
    font-size: 27px;
    line-height: 1;
    letter-spacing: 0.5px;
    color: var(--ink-black);
    text-transform: uppercase;
  }
  .brand-tagline {
    margin-top: 6px;
    font-family: "Open Sans", sans-serif;
    font-weight: 400;
    font-size: 13px;
    line-height: 1;
    color: var(--ink-grey);
    text-transform: uppercase;
  }
  .footer-bands {
    position: absolute;
    left: 0;
    top: 1080px;
    width: 917px;
    height: 120px;
  }
  .footer-line {
    position: absolute;
    left: 405px;
    font-family: "Arimo", Arial, sans-serif;
    font-size: 12.5px;
    color: var(--footer-text);
    white-space: nowrap;
  }
  .footer-line b { font-weight: 700; }
  .line-address { top: 1103px; }
  .line-online { top: 1149px; }
  .label-red { color: var(--brand-red); }
  .label-dark { color: var(--ink-black); }
</style>
</head>
<body>
<main class="letterhead">
  <header class="brand">
    <span class="brand-mark" aria-hidden="true"></span>
    <div class="brand-text">
      <span class="brand-name">Corvane Associates</span>
      <span class="brand-tagline">Accounting, Tax, Business Advice &amp; Legal</span>
    </div>
  </header>

  <svg class="footer-bands" viewBox="0 1080 917 120" aria-hidden="true">
    <rect x="0" y="1107" width="917" height="93" fill="var(--brand-red)"/>
    <polygon points="113,1107 243,1107 177,1176" fill="var(--paper)"/>
    <polygon points="323,1137 363,1091 917,1091 917,1137" fill="var(--ink-black)"/>
  </svg>

  <p class="footer-line line-address">
    <b class="label-red">Address:</b> 48 Kelvin Lane, Northgate Vale, QLD 4051
    <b class="label-red">Mobile:</b> +61 491 570 263
  </p>
  <p class="footer-line line-online">
    <b class="label-dark">E-mail:</b> dana.hollis@corvaneassociates.com.au
    <b class="label-dark">Web:</b> www.corvaneassociates.com.au
  </p>
</main>
</body>
</html>
```